KMB and Employer Sleep Apnea Screening - BROCHURE

Brochure for marketing to KMB Clinics and directly to Employers of commercial drivers for screening of Sleep Apnea. We are a diagnostic sleep facility that offers In-Lab sleep testing and Home sleep testing. Our website: bluperinhealth.com

I put together an idea but i’m Not a designer and welcome your ideas for a brochure.

Two Sided Brochure
TRIM: 99 mm Wide x 210 mm High
with Bleed 105 mm Wide x 216 mm High
allow a 4 mm around card for critical elements

The idea is to print 3 handouts to a 8.5" x 11" card sheet with printing on front and back.
Updates

We are looking for a brochure not a flyer. First time using site and did not see option for brochure. We are looking for a brochure. Thank you for your designs and input.

Target Market(s)

Commercial Truck Drivers

Colors

Designer to choose colors to be used in the design.

Requirements
Must have
• Website: bluperinhealth.com
• Low Out-of-Pocket Cost and Most Insurances Accepted
• Quick Turn Around Time for Sleep Results
• PWRE Accredited
Nice to have
• Images of Commercial Truck or Truck Drivers

```html
<!DOCTYPE html>
<html lang="en">
<head>
<meta charset="utf-8">
<title>KMB Sleep Apnea Screening Brochure</title>
<link href="https://fonts.googleapis.com/css2?family=Oswald:wght@400;500&family=Roboto:wght@400;500&family=Tinos:ital,wght@0,400;0,700;1,400&display=swap" rel="stylesheet">
<style>
  :root {
    --lavender: #d4bcd2;
    --lavender-light: #e3d3e1;
    --plum: #a98ba7;
    --slate: #6f6371;
    --ink: #5e5560;
    --navy: #2f4fa6;
    --white: #ffffff;
    --page: #eeeaee;
    --display: "Oswald", sans-serif;
    --body: "Roboto", sans-serif;
    --serif: "Tinos", serif;
  }
  * { margin: 0; padding: 0; box-sizing: border-box; }
  html, body { width: 960px; height: 1200px; overflow: hidden; background: var(--page); }
  .canvas { position: relative; width: 960px; height: 1200px; }
  .abs { position: absolute; }

  /* front side */
  .front { position: absolute; left: 116px; top: 20px; width: 354px; height: 750px; background: var(--lavender); box-shadow: 0 3px 10px rgba(0,0,0,.2); overflow: hidden; color: var(--ink); }
  .front .company { left: 14px; top: 27px; font: 400 7px var(--body); color: #4a424c; }
  .front .hero { left: 0; top: 44px; width: 354px; height: 220px; background: linear-gradient(90deg, #3b3b3f 0%, #55575c 40%, #d9d9d9 60%, #f4f4f4 100%); }
  .front .hero-title { left: 23px; top: 74px; font-family: var(--display); color: var(--white); line-height: .98; }
  .hero-title .fight, .hero-title .apnea { font-size: 36px; font-weight: 500; display: block; }
  .hero-title .sleep { font-size: 50px; font-weight: 500; display: block; }
  .front .headline { left: 0; width: 354px; top: 276px; text-align: center; font: 500 32px/1.08 var(--display); color: var(--ink); }
  .front .notice { left: 0; top: 368px; width: 354px; height: 50px; background: var(--lavender-light); font: 11px/1.22 var(--serif); text-align: center; padding-top: 11px; color: #4e4650; }
  .front .rule { left: 0; width: 354px; height: 1px; background: var(--lavender-light); }
  .front .tagline { left: 0; width: 354px; top: 436px; text-align: center; font: 400 25px var(--display); color: var(--ink); }
  .front .badge { left: 94px; top: 476px; width: 166px; height: 37px; border-radius: 6px; background: var(--plum); color: var(--white); font: 400 22px/37px var(--display); text-align: center; }
  .front .call { left: 22px; top: 530px; font: 400 24px/1.05 var(--display); color: var(--ink); }
  .front .address { left: 22px; top: 598px; font: 10.5px/1.26 var(--serif); color: #4a424c; }
  .address .web { font-weight: 700; }
  .front .map { left: 204px; top: 532px; width: 126px; height: 126px; background: linear-gradient(135deg, #e6dbe4, #d9cbd8); border: 3px solid var(--white); }
  .front .insurance { left: 0; top: 680px; width: 354px; height: 70px; background: var(--white); text-align: center; font: 400 18px/19px var(--display); color: var(--ink); padding-top: 6px; }
  .insurance .quick { display: block; margin-top: 3px; font: 400 12px/14px var(--display); letter-spacing: .4px; color: var(--plum); }

  /* back side */
  .back { position: relative; width: 823px; height: 388px; background: var(--white); overflow: hidden; box-shadow: 0 3px 10px rgba(0,0,0,.2); }
  .back-flat { position: absolute; left: 69px; top: 788px; }
  .back-turned { position: absolute; left: 491px; top: 20px; width: 354px; height: 750px; }
  .back-turned .back { transform-origin: 0 0; transform: translateY(750px) rotate(-90deg) scale(.911); }
  .back .steps-panel { left: 509px; top: 0; width: 314px; height: 388px; background: var(--lavender); }
  .back .company { left: 0; width: 509px; top: 21px; text-align: center; font: 400 9px var(--body); color: #4a424c; }
  .back .head { top: 46px; font: 500 16px var(--display); white-space: nowrap; }
  .head.symptoms { left: 35px; color: var(--navy); }
  .head.risks { left: 283px; color: #2d2a30; }
  .back .item { font: 400 8.4px/1.15 var(--body); color: #2e3b70; }
  .back .risk { font: 400 8.4px/1.15 var(--body); color: #3a363c; }
  .back .figure { left: 196px; top: 76px; width: 112px; height: 246px; border-radius: 44px 44px 26px 26px; background: linear-gradient(180deg, #f0d36a 0%, #e8c84b 45%, #4a74b8 75%, #3a5d9e 100%); }
  .back .links { left: 0; top: 0; }
  .steps-title { left: 509px; width: 314px; top: 22px; text-align: center; font: 400 19px/1.12 var(--display); color: var(--ink); }
  .step-num { width: 14px; height: 14px; border-radius: 50%; background: #7a6f7c; color: var(--white); font: 8px/14px var(--body); text-align: center; left: 659px; }
  .step-text { left: 509px; width: 314px; text-align: center; font: 10px var(--serif); color: #4a424c; }
  .step-note { left: 509px; width: 314px; text-align: center; font: italic 6.4px var(--serif); color: #4a424c; }
  .back .band { left: 0; top: 330px; width: 823px; height: 38px; background: var(--slate); color: var(--white); text-align: center; font: 400 21px/38px var(--display); }
</style>
</head>
<body>
<div class="canvas">

  <section class="front" aria-label="Brochure front">
    <p class="abs company">Restwell Sleep Diagnostics LLC.</p>
    <div class="abs hero" role="img" aria-label="Photo of a yawning truck driver in his cab"></div>
    <h1 class="abs hero-title"><span class="fight">FIGHT</span><span class="sleep">SLEEP</span><span class="apnea">APNEA</span></h1>
    <h2 class="abs headline">KMB PHYSICAL REQUIRES<br>TESTING FOR SLEEP APNEA</h2>
    <p class="abs notice">Your KMB Medical Examiner has given you 3 months to check for<br>and correct a potential concern: SLEEP APNEA</p>
    <div class="abs rule" style="top:494px"></div>
    <p class="abs tagline">DON’T STRESS - DON’T WAIT</p>
    <div class="abs badge">PWRE ACCREDITED</div>
    <p class="abs call">CALL TODAY<br>702-555-0148</p>
    <p class="abs address">2480 Orchard Crest Drive, Suite 7C<br>Las Vegas, NV 89119<br>P: (702) 555-0148&nbsp; F: (702) 555-0192<br>hello@bluperinhealth.com<br><span class="web">www.bluperinhealth.com</span></p>
    <div class="abs map" role="img" aria-label="Street map showing the clinic location"></div>
    <p class="abs insurance">LOW OUT-OF-POCKET COST<br>AND MOST INSURANCES ACCEPTED<span class="quick">QUICK TURN AROUND TIME FOR SLEEP RESULTS</span></p>
  </section>

  <div class="back-turned">
    <section class="back" aria-label="Brochure back, turned">
      <div class="abs steps-panel"></div>
      <p class="abs company">Restwell Sleep Diagnostics LLC.</p>
      <h3 class="abs head symptoms">SYMPTOMS OF SLEEP APNEA</h3>
      <h3 class="abs head risks">RISK FACTORS FOR SLEEP APNEA</h3>
      <svg class="abs links" width="509" height="330" aria-hidden="true">
        <g stroke="#3557ad" stroke-width="1" fill="none">
          <path d="M119 112 L230 100"/><path d="M158 146 L232 112"/><path d="M122 170 L224 134"/><path d="M94 194 L210 168"/><path d="M139 220 L210 196"/><path d="M83 246 L210 238"/><path d="M154 266 L250 230"/><path d="M141 294 L240 210"/>
        </g>
        <g stroke="#333" stroke-width="1" fill="none">
          <path d="M325 112 L280 128"/><path d="M325 150 L280 160"/><path d="M325 186 L290 176"/><path d="M325 214 L296 214"/><path d="M325 239 L300 239"/><path d="M325 264 L300 264"/><path d="M325 290 L300 288"/>
        </g>
        <g fill="#3557ad"><circle cx="119" cy="112" r="3"/><circle cx="158" cy="146" r="3"/><circle cx="122" cy="170" r="3"/><circle cx="94" cy="194" r="3"/><circle cx="139" cy="220" r="3"/><circle cx="83" cy="246" r="3"/><circle cx="154" cy="266" r="3"/><circle cx="141" cy="294" r="3"/></g>
        <g fill="#333"><circle cx="325" cy="112" r="3"/><circle cx="325" cy="150" r="3"/><circle cx="325" cy="186" r="3"/><circle cx="325" cy="214" r="3"/><circle cx="325" cy="239" r="3"/><circle cx="325" cy="264" r="3"/><circle cx="325" cy="290" r="3"/></g>
      </svg>
      <div class="abs figure" role="img" aria-label="Cartoon truck driver in cap and safety vest holding a beer"></div>
      <p class="abs item" style="left:35px;top:103px">Concentration and<br>memory problems</p>
      <p class="abs item" style="left:35px;top:137px">Disturbed sleep and<br>Excessive daytime sleepiness</p>
      <p class="abs item" style="left:35px;top:166px">Morning Headaches</p>
      <p class="abs item" style="left:35px;top:190px">Loud Snoring</p>
      <p class="abs item" style="left:35px;top:211px">Gasping or choking while<br>sleeping</p>
      <p class="abs item" style="left:35px;top:242px">Nausea</p>
      <p class="abs item" style="left:35px;top:262px">Frequent Nighttime Urination</p>
      <p class="abs item" style="left:35px;top:285px">Irritability and/or feelings<br>of depress</p>
      <p class="abs risk" style="left:334px;top:103px">Having a recessed chin, small jaw<br>or a large overbite</p>
      <p class="abs risk" style="left:334px;top:141px">A large neck size (17 inches or<br>greater for men, 16 inches or<br>greater for women)</p>
      <p class="abs risk" style="left:334px;top:181px">Having a small upper airway</p>
      <p class="abs risk" style="left:334px;top:209px">Tobacco and alcohol use</p>
      <p class="abs risk" style="left:334px;top:234px">Being overweight</p>
      <p class="abs risk" style="left:334px;top:259px">Being age 40 or older</p>
      <p class="abs risk" style="left:334px;top:285px">A family history of sleep apnea</p>
      <h3 class="abs steps-title">THIS MAY REQUIRE<br>THE FOLLOWING STEPS</h3>
      <div class="abs step-num" style="top:71px">1</div>
      <p class="abs step-text" style="top:91px">Conduct Sleep Apnea Testing</p>
      <p class="abs step-note" style="top:104px">(If negative finished go to step 5. If positive continue to steps 2 through 5)</p>
      <div class="abs step-num" style="top:127px">2</div>
      <p class="abs step-text" style="top:147px">CPAP/BiPAP/ASV Titration</p>
      <div class="abs step-num" style="top:175px">3</div>
      <p class="abs step-text" style="top:195px">Acquire Home PAP Equipment</p>
      <div class="abs step-num" style="top:223px">4</div>
      <p class="abs step-text" style="top:243px">30 Days on Home PAP Therapy</p>
      <div class="abs step-num" style="top:271px">5</div>
      <p class="abs step-text" style="top:291px">Follow-up KMB Appointment Before 3 Month Period Expires</p>
      <p class="abs band">COMMERCIAL DRIVERS CAN MANAGE SLEEP APNEA &amp; MAINTAIN THEIR CDL</p>
    </section>
  </div>

  <div class="back-flat">
    <section class="back" aria-label="Brochure back">
      <div class="abs steps-panel"></div>
      <p class="abs company">Restwell Sleep Diagnostics LLC.</p>
      <h3 class="abs head symptoms">SYMPTOMS OF SLEEP APNEA</h3>
      <h3 class="abs head risks">RISK FACTORS FOR SLEEP APNEA</h3>
      <svg class="abs links" width="509" height="330" aria-hidden="true">
        <g stroke="#3557ad" stroke-width="1" fill="none">
          <path d="M119 112 L230 100"/><path d="M158 146 L232 112"/><path d="M122 170 L224 134"/><path d="M94 194 L210 168"/><path d="M139 220 L210 196"/><path d="M83 246 L210 238"/><path d="M154 266 L250 230"/><path d="M141 294 L240 210"/>
        </g>
        <g stroke="#333" stroke-width="1" fill="none">
          <path d="M325 112 L280 128"/><path d="M325 150 L280 160"/><path d="M325 186 L290 176"/><path d="M325 214 L296 214"/><path d="M325 239 L300 239"/><path d="M325 264 L300 264"/><path d="M325 290 L300 288"/>
        </g>
        <g fill="#3557ad"><circle cx="119" cy="112" r="3"/><circle cx="158" cy="146" r="3"/><circle cx="122" cy="170" r="3"/><circle cx="94" cy="194" r="3"/><circle cx="139" cy="220" r="3"/><circle cx="83" cy="246" r="3"/><circle cx="154" cy="266" r="3"/><circle cx="141" cy="294" r="3"/></g>
        <g fill="#333"><circle cx="325" cy="112" r="3"/><circle cx="325" cy="150" r="3"/><circle cx="325" cy="186" r="3"/><circle cx="325" cy="214" r="3"/><circle cx="325" cy="239" r="3"/><circle cx="325" cy="264" r="3"/><circle cx="325" cy="290" r="3"/></g>
      </svg>
      <div class="abs figure" role="img" aria-label="Cartoon truck driver in cap and safety vest holding a beer"></div>
      <p class="abs item" style="left:35px;top:103px">Concentration and<br>memory problems</p>
      <p class="abs item" style="left:35px;top:137px">Disturbed sleep and<br>Excessive daytime sleepiness</p>
      <p class="abs item" style="left:35px;top:166px">Morning Headaches</p>
      <p class="abs item" style="left:35px;top:190px">Loud Snoring</p>
      <p class="abs item" style="left:35px;top:211px">Gasping or choking while<br>sleeping</p>
      <p class="abs item" style="left:35px;top:242px">Nausea</p>
      <p class="abs item" style="left:35px;top:262px">Frequent Nighttime Urination</p>
      <p class="abs item" style="left:35px;top:285px">Irritability and/or feelings<br>of depress</p>
      <p class="abs risk" style="left:334px;top:103px">Having a recessed chin, small jaw<br>or a large overbite</p>
      <p class="abs risk" style="left:334px;top:141px">A large neck size (17 inches or<br>greater for men, 16 inches or<br>greater for women)</p>
      <p class="abs risk" style="left:334px;top:181px">Having a small upper airway</p>
      <p class="abs risk" style="left:334px;top:209px">Tobacco and alcohol use</p>
      <p class="abs risk" style="left:334px;top:234px">Being overweight</p>
      <p class="abs risk" style="left:334px;top:259px">Being age 40 or older</p>
      <p class="abs risk" style="left:334px;top:285px">A family history of sleep apnea</p>
      <h3 class="abs steps-title">THIS MAY REQUIRE<br>THE FOLLOWING STEPS</h3>
      <div class="abs step-num" style="top:71px">1</div>
      <p class="abs step-text" style="top:91px">Conduct Sleep Apnea Testing</p>
      <p class="abs step-note" style="top:104px">(If negative finished go to step 5. If positive continue to steps 2 through 5)</p>
      <div class="abs step-num" style="top:127px">2</div>
      <p class="abs step-text" style="top:147px">CPAP/BiPAP/ASV Titration</p>
      <div class="abs step-num" style="top:175px">3</div>
      <p class="abs step-text" style="top:195px">Acquire Home PAP Equipment</p>
      <div class="abs step-num" style="top:223px">4</div>
      <p class="abs step-text" style="top:243px">30 Days on Home PAP Therapy</p>
      <div class="abs step-num" style="top:271px">5</div>
      <p class="abs step-text" style="top:291px">Follow-up KMB Appointment Before 3 Month Period Expires</p>
      <p class="abs band">COMMERCIAL DRIVERS CAN MANAGE SLEEP APNEA &amp; MAINTAIN THEIR CDL</p>
    </section>
  </div>

</div>
</body>
</html>
```